Lumavorne Business Card Design

I need a business card design for a new Business, that is focused on Custom Made Designer Furniture. that is aimed at the mid to high end markets. I would like a card that would in some way portray what I do for my clients in the way we are able to make any idea a reality and also work within a set budget to meet their requirements.
I like quite contemporary colours and styling and I want the final design to communicate a Contemporary and Professional image.

Target Market(s)

mid to high end market

Industry/Entity Type

Business

Contact Information for Business Card

Lumavorne
Harold Brenning
82 Wendle Ave, Tarrow, Auckland, New Zealand 0927.

Requirements
Nice to have
• I would also like to utilize the spot gloss or raised print on my cards

```html
<!DOCTYPE html>
<html lang="en">
<head>
<meta charset="utf-8">
<title>Lumavorne Business Card</title>
<link rel="stylesheet" href="https://fonts.googleapis.com/css2?family=Roboto:wght@300;700&display=swap">
<style>
  :root {
    --backdrop: #e9a993;
    --card: #1b1b1d;
    --brand-blue: #1f9bd7;
    --name-grey: #c4c4c6;
    --card-shadow: rgba(90, 40, 25, 0.28);
  }
  * { box-sizing: border-box; margin: 0; padding: 0; }
  html, body {
    width: 1200px;
    height: 900px;
    overflow: hidden;
  }
  body {
    background: var(--backdrop);
    font-family: "Roboto", Arial, sans-serif;
  }
  .business-card {
    position: absolute;
    left: 150px;
    top: 200px;
    width: 900px;
    height: 500px;
    background: var(--card);
    box-shadow: 0 18px 40px var(--card-shadow);
  }
  .brand-name {
    position: absolute;
    left: 58px;
    top: 56px;
    font-size: 46px;
    font-weight: 700;
    color: var(--brand-blue);
    letter-spacing: -0.5px;
  }
  .person-name {
    position: absolute;
    left: 56px;
    top: 108px;
    font-size: 62px;
    font-weight: 300;
    color: var(--name-grey);
    letter-spacing: -1px;
  }
  .brand-square {
    position: absolute;
    right: 72px;
    top: 140px;
    width: 150px;
    height: 150px;
    background: var(--brand-blue);
  }
  .address {
    position: absolute;
    left: 58px;
    top: 352px;
    font-style: normal;
    font-size: 23px;
    font-weight: 700;
    line-height: 1.4;
    color: var(--brand-blue);
  }
</style>
</head>
<body>
  <section class="business-card">
    <p class="brand-name">Lumavorne</p>
    <h1 class="person-name">Harold Brenning</h1>
    <div class="brand-square"></div>
    <address class="address">
      82 Wendle Ave, Tarrow, Auckland<br>
      New Zealand 0927
    </address>
  </section>
</body>
</html>
```